Geschäftspapiere für Unternehmen aus Not- und Sicherheitsbeleuchtungsbranche
Zielgruppe
Wir sind ein Unternehmen der Not- und Sicherheitsbeleuchtungsbranche und arbeiten vornehmlich mit dem deutschen Elektrogroßhandel zusammen.
Aufgabenstellung
WIr möchten nicht nur Schreibblöcke drucken, wir benötigen die Vorlage auch als Word-Datei für Geschäftsbriefe.
Orientierung und Farbwahl gemäß unserer Website. Im Anhang finden Sie bereits das aktuelle Briefdesign. Dieses verbraucht jedoch zu viel Platz und liegt uns nicht als Word vor. Die Daten können übernommen werden, ergänzt muss noch die UST-ID werden: DE718206359

```html
<!DOCTYPE html>
<html lang="de">
<head>
<meta charset="utf-8">
<title>Lumaris – Geschäftspapiere</title>
<link href="https://fonts.googleapis.com/css2?family=Montserrat:wght@400;500;700&display=swap" rel="stylesheet">
<style>
  :root{
    --bg:#e3e8e9;
    --paper:#ffffff;
    --magenta:#b0086a;
    --slate:#5f6670;
    --ink:#2a2d31;
    --ghost:#ececee;
    --grid:#e2e3e6;
  }
  *{box-sizing:border-box;margin:0;padding:0}
  html,body{width:1200px;height:674px;overflow:hidden}
  body{background:var(--bg);font-family:"Montserrat",sans-serif;color:var(--ink);position:relative}
  .sheet{position:absolute;top:77px;width:368px;height:520px;background:var(--paper);box-shadow:0 6px 18px rgba(40,50,60,.18);overflow:hidden}
  .sheet--follow{left:24px}
  .sheet--letter{left:416px}
  .sheet--pad{left:808px}

  .brand{position:absolute;display:flex;align-items:center;gap:6px;font-weight:500;letter-spacing:.12em;color:var(--slate)}
  .brand__square{width:12px;height:12px;background:var(--magenta)}
  .watermark{position:absolute;left:50%;top:44%;width:150px;height:120px;transform:translate(-50%,-50%);border:14px solid var(--ghost)}

  .footer-bands{position:absolute;left:0;bottom:0;width:100%;height:60px}

  .sender-line{position:absolute;left:34px;top:62px;font-size:4.5px;padding-bottom:2px;border-bottom:1px solid var(--magenta);white-space:nowrap}

  .addr{position:absolute;font-size:5.5px;line-height:1.45}
  .addr strong{color:var(--magenta);font-weight:700}
  .addr--side{right:26px;top:92px;padding-left:8px;border-left:1px solid var(--slate)}
  .contact{display:flex;align-items:center;gap:4px}
  .contact svg{width:5px;height:5px;fill:var(--magenta)}

  .footer-text{position:absolute;left:24px;right:16px;bottom:62px;display:flex;gap:14px;font-size:4.4px;line-height:1.45}
  .footer-text strong{font-weight:700}
  .footer-text .label{color:var(--magenta);font-weight:700}

  .pad-head{position:absolute;left:24px;right:20px;top:22px;height:40px}
  .pad-addr{position:absolute;top:30px;font-size:5px;line-height:1.45;padding-left:7px;border-left:1px solid var(--slate)}
  .pad-addr strong{color:var(--magenta);font-weight:700}
  .grid{position:absolute;left:24px;right:24px;top:78px;bottom:26px;
    background-image:linear-gradient(var(--grid) 1px,transparent 1px),linear-gradient(90deg,var(--grid) 1px,transparent 1px);
    background-size:8px 8px}
</style>
</head>
<body>

<section class="sheet sheet--follow" aria-label="Folgeseite">
  <div class="watermark" aria-hidden="true"></div>
  <svg class="footer-bands" viewBox="0 0 368 60" preserveAspectRatio="none" aria-hidden="true">
    <rect x="0" y="28" width="150" height="8" fill="var(--magenta)"/>
    <polygon points="160,40 368,40 368,60 140,60" fill="var(--slate)"/>
  </svg>
</section>

<section class="sheet sheet--letter" aria-label="Briefbogen">
  <p class="sender-line">Lumaris GmbH · Lindenweg 7 · D-83123 Altfeld</p>
  <div class="brand" style="right:26px;top:48px;font-size:12px"><span class="brand__square"></span>LUMARIS</div>
  <div class="addr addr--side">
    <strong>Lumaris GmbH</strong><br>Lindenweg 7<br>D-83123 Altfeld
    <div class="contact"><svg viewBox="0 0 10 10"><path d="M2 0h2l1 3-1.5 1a6 6 0 0 0 2.5 2.5L7 5l3 1v2a2 2 0 0 1-2 2A8 8 0 0 1 0 2a2 2 0 0 1 2-2z"/></svg>08661 30472 18</div>
    <div class="contact"><svg viewBox="0 0 10 10"><rect x="0" y="2" width="10" height="6"/></svg>info@lumaris-licht.de</div>
    <div class="contact"><svg viewBox="0 0 10 10"><circle cx="5" cy="5" r="5"/></svg>www.lumaris-licht.de</div>
  </div>
  <div class="watermark" aria-hidden="true"></div>
  <div class="footer-text">
    <div><strong>Lumaris GmbH</strong><br>Lindenweg 7<br>D-83123 Altfeld</div>
    <div><span class="label">Geschäftsführer</span><br>Moritz Kelbing<br>Managing Director</div>
    <div>08661 30472 18<br>info@lumaris-licht.de<br>www.lumaris-licht.de</div>
    <div><strong>Amtsgericht Altfeld</strong><br>HRB 40527<br>USt.-ID DE718206359</div>
    <div>Bankverbindung Sparkasse Altfeld<br>BLZ 700 123 45<br>IBAN: DE00 7001 2345 0012 3456 78<br>BIC: ALTFDEX1XXX</div>
  </div>
  <svg class="footer-bands" viewBox="0 0 368 60" preserveAspectRatio="none" aria-hidden="true">
    <rect x="0" y="28" width="170" height="8" fill="var(--magenta)"/>
    <polygon points="180,40 368,40 368,60 160,60" fill="var(--slate)"/>
  </svg>
</section>

<section class="sheet sheet--pad" aria-label="Schreibblock">
  <div class="pad-head">
    <div class="brand" style="left:0;top:0;font-size:13px"><span class="brand__square"></span>LUMARIS</div>
    <div class="pad-addr" style="left:170px"><strong>Lumaris GmbH</strong><br>Lindenweg 7<br>D-83123 Altfeld</div>
    <div class="pad-addr" style="left:246px">
      <div class="contact"><svg viewBox="0 0 10 10" style="width:5px;height:5px;fill:var(--magenta)"><path d="M2 0h2l1 3-1.5 1a6 6 0 0 0 2.5 2.5L7 5l3 1v2a2 2 0 0 1-2 2A8 8 0 0 1 0 2a2 2 0 0 1 2-2z"/></svg>08661 30472 18</div>
      <div class="contact"><svg viewBox="0 0 10 10" style="width:5px;height:5px;fill:var(--magenta)"><rect x="0" y="2" width="10" height="6"/></svg>info@lumaris-licht.de</div>
      <div class="contact"><svg viewBox="0 0 10 10" style="width:5px;height:5px;fill:var(--magenta)"><circle cx="5" cy="5" r="5"/></svg>www.lumaris-licht.de</div>
    </div>
  </div>
  <div class="grid" aria-hidden="true"></div>
</section>

</body>
</html>
```